" A empresa atua em dois segmentos: 1) atendimento psicológico de crianças, adolescentes e adultos e 2) recrutamento, seleçao e treinamento de pessoas. A proposta é trabalhar com o desenvolvimento humano em suas diversas dimensoes. "

```html
<!DOCTYPE html>
<html lang="pt-BR">
<head>
<meta charset="utf-8">
<title>Rumo Vivo – Cartão de visita</title>
<link rel="stylesheet" href="https://fonts.googleapis.com/css2?family=Exo+2:wght@400;500&display=swap">
<style>
  :root {
    --teal: #1a9e96;
    --teal-dark: #13847d;
    --ink: #5e6366;
    --paper: #ffffff;
    --backdrop: #e9ebec;
  }
  * { margin: 0; padding: 0; box-sizing: border-box; }
  html, body {
    width: 1200px; height: 1200px; overflow: hidden;
    background: var(--backdrop);
    font-family: "Exo 2", sans-serif;
  }
  .canvas { position: relative; width: 1200px; height: 1200px; }

  .card {
    position: absolute; left: 170px;
    width: 860px; height: 500px;
    background: var(--paper);
    border-radius: 26px;
    overflow: hidden;
    box-shadow: 0 6px 22px rgba(0,0,0,.12);
  }
  .card--front { top: 70px; }
  .card--back  { top: 630px; }

  /* front */
  .front-mark {
    position: absolute; left: 50%; top: 50%;
    transform: translate(-50%, -50%);
    display: flex; flex-direction: column; align-items: center; gap: 26px;
  }
  .front-mark__dot {
    width: 250px; height: 250px; border-radius: 50%;
    background: var(--teal);
  }
  .brand-name {
    color: var(--teal);
    font-weight: 400;
    white-space: nowrap;
  }
  .front-mark .brand-name { font-size: 46px; }

  /* back */
  .back-panel { position: absolute; inset: 0; width: 100%; height: 100%; }
  .back-panel polygon { fill: var(--teal); }

  .contact { position: absolute; left: 46px; color: var(--paper); }
  .contact--person { top: 70px; }
  .contact__name { font-size: 42px; font-weight: 500; line-height: 1.1; }
  .contact__role { font-size: 25px; line-height: 1.3; }
  .contact__email { font-size: 25px; margin-top: 28px; }
  .contact--address { top: 290px; font-size: 25px; line-height: 34px; }

  .back-brand {
    position: absolute; right: 60px; bottom: 72px;
    display: flex; align-items: center; gap: 18px;
  }
  .back-brand__dot {
    width: 80px; height: 80px; border-radius: 50%;
    background: var(--teal);
  }
  .back-brand .brand-name { font-size: 50px; }
</style>
</head>
<body>
<main class="canvas">

  <section class="card card--front" aria-label="Frente do cartão">
    <div class="front-mark">
      <div class="front-mark__dot"></div>
      <span class="brand-name">Rumo Vivo</span>
    </div>
  </section>

  <section class="card card--back" aria-label="Verso do cartão">
    <svg class="back-panel" viewBox="0 0 860 500" preserveAspectRatio="none" aria-hidden="true">
      <polygon points="0,0 520,0 410,500 0,500"/>
    </svg>

    <div class="contact contact--person">
      <p class="contact__name">Marina Souto</p>
      <p class="contact__role">cargo</p>
      <p class="contact__email">marina@rumovivo.com.br</p>
    </div>

    <div class="contact contact--address">
      <p>Rua Aurora n°215</p>
      <p>São Paulo &nbsp;S.P.</p>
      <p>11 4000-1234</p>
      <p>11 4000-5678</p>
      <p>www.rumovivo.com.br</p>
    </div>

    <div class="back-brand">
      <div class="back-brand__dot"></div>
      <span class="brand-name">Rumo Vivo</span>
    </div>
  </section>

</main>
</body>
</html>
```